Business Card design for new private practice opening

I need a business card design for my new private practice with my new logo uploaded as a file
On the front the logo
On the back: maybe a small logo somewhere?
Priv. Doz. DDr. Corinna Vestaluk
Fachärztin für Allgemein- & Viszeralchirurgie
Address: xxx
Tel: xxx
Mobil:xxx
Webseite:xxx
Email:xxx

Contact Information for Business Card

See project description above for details

Requirements
Nice to have
• I would like the colors of the logo incorporated into the business card

```html
<!DOCTYPE html>
<html lang="de">
<head>
<meta charset="utf-8">
<title>Vestaluk Chirurgie – Visitenkarte</title>
<link href="https://fonts.googleapis.com/css2?family=Montserrat:wght@300;500;700&display=swap" rel="stylesheet">
<style>
  :root {
    --teal: #46b9b6;
    --band: #8a8a8a;
    --brand-grey: #858585;
    --ink: #333333;
    --paper: #ffffff;
    --stage: #e6e6e6;
    --gap: #d4d3d3;
  }
  * { margin: 0; padding: 0; box-sizing: border-box; }
  html, body { width: 1069px; height: 1200px; overflow: hidden; }
  body {
    background: radial-gradient(ellipse at center, #dcdcdc 0%, var(--stage) 60%, #f2f2f2 100%);
    font-family: "Montserrat", sans-serif;
    position: relative;
  }
  .card {
    position: absolute;
    left: 131px;
    width: 759px;
    height: 443px;
    background: var(--paper);
    overflow: hidden;
  }
  .card--back { top: 112px; }
  .card--front { top: 594px; }
  .card-gap {
    position: absolute;
    left: 131px; top: 555px;
    width: 759px; height: 39px;
    background: var(--gap);
  }
  .band { position: absolute; left: 0; width: 759px; height: 34px; }
  .band--top { top: 0; }
  .band--bottom { bottom: 0; }
  .band path { fill: var(--band); }

  .holder-name {
    position: absolute; left: 35px; top: 75px;
    font-weight: 700; font-size: 28.4px; color: var(--teal);
    white-space: nowrap;
  }
  .holder-title {
    position: absolute; left: 35px; top: 114px;
    font-weight: 300; font-size: 20.7px; color: var(--teal);
    white-space: nowrap;
  }
  .contact-list { position: absolute; left: 31px; top: 0; list-style: none; }
  .contact-list li {
    position: absolute; left: 0;
    display: flex; align-items: center; gap: 16px;
    font-weight: 500; font-size: 26.9px; color: var(--ink);
    white-space: nowrap;
  }
  .contact-list svg { width: 22px; height: 22px; fill: var(--teal); flex: none; }

  .brand { position: absolute; display: flex; align-items: center; }
  .brand-dot { border-radius: 50%; border: 3px solid var(--brand-grey); flex: none; }
  .brand-name {
    color: var(--brand-grey); font-weight: 500;
    white-space: nowrap;
  }
  .brand--small { left: 432px; top: 179px; gap: 14px; }
  .brand--small .brand-dot { width: 82px; height: 82px; }
  .brand--small .brand-name { font-size: 20px; }
  .brand--large { left: 119px; top: 143px; gap: 28px; }
  .brand--large .brand-dot { width: 154px; height: 154px; border-width: 4px; }
  .brand--large .brand-name { font-size: 38px; }
</style>
</head>
<body>

<section class="card card--back">
  <svg class="band band--top" viewBox="0 0 759 34"><path d="M15 0H739V10a9 9 0 0 1-9 9H561c-12 0-18 14-35 14H227c-17 0-23-14-35-14H24a9 9 0 0 1-9-9z"/></svg>

  <h1 class="holder-name">Priv. Doz. DDr. Corinna Vestaluk</h1>
  <p class="holder-title">Fachärztin für Allgemein- &amp; Viszeralchirurgie</p>

  <ul class="contact-list">
    <li style="top:183px">
      <svg viewBox="0 0 24 24"><path d="M7 1h10a2 2 0 0 1 2 2v18a2 2 0 0 1-2 2H7a2 2 0 0 1-2-2V3a2 2 0 0 1 2-2zm0 3v14h10V4zm5 15.5a1 1 0 1 0 0 2 1 1 0 0 0 0-2z"/></svg>
      122-899 5457
    </li>
    <li style="top:224px">
      <svg viewBox="0 0 24 24"><path d="M6.6 10.8a15 15 0 0 0 6.6 6.6l2.2-2.2a1 1 0 0 1 1-.25 11.4 11.4 0 0 0 3.6.6 1 1 0 0 1 1 1V20a1 1 0 0 1-1 1A17 17 0 0 1 3 4a1 1 0 0 1 1-1h3.5a1 1 0 0 1 1 1c0 1.25.2 2.45.6 3.6a1 1 0 0 1-.25 1z"/></svg>
      123-45465 6565
    </li>
    <li style="top:260px">
      <svg viewBox="0 0 24 24"><path d="M2 5h20v2l-10 6L2 7zm0 4.3l10 6 10-6V19H2z"/></svg>
      abcd@email.com
    </li>
    <li style="top:298px">
      <svg viewBox="0 0 24 24"><path d="M12 2a10 10 0 1 0 0 20 10 10 0 0 0 0-20zm-1 2.1V8H7.6A8 8 0 0 1 11 4.1zm2 0A8 8 0 0 1 16.4 8H13zM4.3 10h6.7v4H4.3a8 8 0 0 1 0-4zm8.7 0h6.7a8 8 0 0 1 0 4H13zm-5.4 6H11v3.9A8 8 0 0 1 7.6 16zm5.4 0h3.4A8 8 0 0 1 13 19.9z"/></svg>
      www.website.com
    </li>
    <li style="top:340px">
      <svg viewBox="0 0 24 24"><path d="M12 1a8 8 0 0 0-8 8c0 6 8 14 8 14s8-8 8-14a8 8 0 0 0-8-8zm0 11a3 3 0 1 1 0-6 3 3 0 0 1 0 6z"/></svg>
      Youraddress
    </li>
  </ul>

  <div class="brand brand--small">
    <span class="brand-dot"></span>
    <span class="brand-name">Vestaluk Chirurgie</span>
  </div>

  <svg class="band band--bottom" viewBox="0 0 759 34"><path d="M15 34H739V24a9 9 0 0 0-9-9H561c-12 0-18-14-35-14H227c-17 0-23 14-35 14H24a9 9 0 0 0-9 9z"/></svg>
</section>

<div class="card-gap"></div>

<section class="card card--front">
  <svg class="band band--top" viewBox="0 0 759 34"><path d="M15 0H739V10a9 9 0 0 1-9 9H561c-12 0-18 14-35 14H227c-17 0-23-14-35-14H24a9 9 0 0 1-9-9z"/></svg>

  <div class="brand brand--large">
    <span class="brand-dot"></span>
    <span class="brand-name">Vestaluk Chirurgie</span>
  </div>

  <svg class="band band--bottom" viewBox="0 0 759 34"><path d="M15 34H739V24a9 9 0 0 0-9-9H561c-12 0-18-14-35-14H227c-17 0-23 14-35 14H24a9 9 0 0 0-9 9z"/></svg>
</section>

</body>
</html>
```